Logo for Quill Partners LLC needs a design

This logo will be for a food handler and restaurant manager training business located. I am a registered trainer and proctor for DineGuard, the United Kitchen Guild. colors options should be black, white, blue, silver or something else bold. The file that I have sent needs to be on the card somewhere, small.
Updates

need to have the DineGuard logo that I added on the card. QUILL stands for quality upkeep in local lunchrooms.

Logo Text

Dennis JonesStar ,Partners LLC. , Registered trainer and proctorwith DineGuard.

```html
<!DOCTYPE html>
<html lang="en">
<head>
<meta charset="utf-8">
<title>Quill Partners LLC – Business Card</title>
<link href="https://fonts.googleapis.com/css2?family=Montserrat:wght@400;500;600;700&display=swap" rel="stylesheet">
<style>
  :root {
    --navy: #24378a;
    --navy-deep: #1d2d74;
    --sky: #1ea0e2;
    --ink: #1b1b1b;
    --paper: #ffffff;
    --backdrop: #1f1f1f;
  }
  * { margin: 0; padding: 0; box-sizing: border-box; }
  html, body {
    width: 1200px; height: 930px; overflow: hidden;
    background: var(--backdrop);
    font-family: "Montserrat", sans-serif;
  }
  .canvas { position: relative; width: 1200px; height: 930px; }

  .card {
    position: absolute; width: 540px; height: 310px;
    border-radius: 18px; overflow: hidden;
  }

  /* Back side */
  .card-back {
    left: 60px; top: 130px;
    background: linear-gradient(135deg, #2f4596 0%, var(--navy) 55%, var(--navy-deep) 100%);
    color: var(--paper);
  }
  .card-back .brand { position: absolute; left: 110px; top: 112px; }

  .brand-name { font-weight: 700; font-size: 31px; letter-spacing: -0.3px; line-height: 1; }
  .brand-sub { font-weight: 400; font-size: 17px; text-align: right; margin-top: 2px; padding-right: 40px; }
  .brand-tagline { font-weight: 500; font-size: 10.5px; margin-top: 4px; white-space: nowrap; }

  /* Front side */
  .card-front { left: 600px; top: 490px; background: var(--paper); color: var(--ink); }
  .card-front .brand { position: absolute; left: 30px; top: 100px; }
  .card-front .brand-name { color: var(--navy); font-size: 27px; }
  .card-front .brand-sub { color: var(--sky); font-size: 15px; padding-right: 36px; }
  .card-front .brand-tagline { font-size: 9.5px; }

  .partner-mark { position: absolute; right: 28px; top: 26px; text-align: left; }
  .partner-mark .mark-name { display: flex; align-items: center; gap: 6px; color: var(--sky); font-weight: 700; font-size: 17px; }
  .partner-mark .mark-dot { width: 10px; height: 10px; border-radius: 50%; background: var(--navy); }
  .partner-mark .mark-note { font-size: 7px; color: #444; line-height: 1.3; margin-top: 3px; font-family: "Montserrat", sans-serif; }

  .side-tab { position: absolute; right: 0; top: 98px; width: 9px; height: 32px; background: var(--navy); }

  .person { position: absolute; right: 30px; top: 104px; text-align: right; }
  .person-name { color: var(--sky); font-weight: 500; font-size: 25px; letter-spacing: 0.5px; line-height: 1; }
  .person-role { font-size: 14px; margin-top: 3px; }

  .rule { position: absolute; left: 70px; right: 24px; top: 176px; height: 1.5px; background: var(--sky); }

  .contacts { position: absolute; left: 52px; top: 186px; list-style: none; font-size: 15px; line-height: 21px; }
  .contacts li { display: flex; align-items: center; gap: 8px; }
  .contacts svg { width: 10px; height: 10px; flex: none; }

  .address { position: absolute; right: 28px; top: 188px; text-align: right; font-size: 15px; line-height: 21px; }

  .band { position: absolute; left: 0; bottom: 0; width: 540px; height: 80px; }
</style>
</head>
<body>
<main class="canvas">

  <section class="card card-back" aria-label="Card back">
    <div class="brand">
      <div class="brand-name">Harold PikeQuill</div>
      <div class="brand-sub">Partners LLC.</div>
      <div class="brand-tagline">Registered trainer and proctor with DineGuard.</div>
    </div>
  </section>

  <section class="card card-front" aria-label="Card front">
    <div class="partner-mark">
      <div class="mark-name"><span>DineGuard</span><span class="mark-dot"></span></div>
      <div class="mark-note">Registered DineGuard Proctor<br>&amp; Certified DineGuard Instructor</div>
    </div>

    <div class="side-tab"></div>

    <div class="brand">
      <div class="brand-name">Harold PikeQuill</div>
      <div class="brand-sub">Partners LLC.</div>
      <div class="brand-tagline">Registered trainer and proctor with DineGuard.</div>
    </div>

    <div class="person">
      <div class="person-name">DANIEL FORD</div>
      <div class="person-role">Director</div>
    </div>

    <div class="rule"></div>

    <ul class="contacts">
      <li><svg viewBox="0 0 10 10"><path d="M2 1 L4 1 L4.6 3 L3.4 3.8 Q4.4 5.8 6.2 6.6 L7 5.4 L9 6 L9 8 Q5 9 2.5 6.5 Q0.8 4.5 2 1Z" fill="#1e6fd0"/></svg>03 5550 1482</li>
      <li><svg viewBox="0 0 10 10"><rect x="2.5" y="0.5" width="5" height="9" rx="1" fill="none" stroke="#1e6fd0" stroke-width="1.2"/><circle cx="5" cy="8" r="0.6" fill="#1e6fd0"/></svg>0400 555 219</li>
      <li><svg viewBox="0 0 10 10"><rect x="0.6" y="2" width="8.8" height="6" fill="none" stroke="#1e6fd0" stroke-width="1.1"/><path d="M0.8 2.3 L5 5.5 L9.2 2.3" fill="none" stroke="#1e6fd0" stroke-width="1.1"/></svg>info@haroldpikequill.com</li>
      <li><svg viewBox="0 0 10 10"><circle cx="5" cy="5" r="4.2" fill="none" stroke="#1e6fd0" stroke-width="1"/><ellipse cx="5" cy="5" rx="1.8" ry="4.2" fill="none" stroke="#1e6fd0" stroke-width="0.8"/><path d="M1 5 H9" stroke="#1e6fd0" stroke-width="0.8"/></svg>www.haroldpikequill.com</li>
    </ul>

    <div class="address">1185 Linden Lane<br>Westfield Park, MA 02100</div>

    <svg class="band" viewBox="0 0 540 80" preserveAspectRatio="none" aria-hidden="true">
      <path d="M0 58 L290 58 C318 58 322 22 352 22 L540 22 L540 80 L0 80 Z" fill="var(--navy)"/>
      <path d="M0 54 L286 54 C312 54 316 18 346 18 L540 18" fill="none" stroke="var(--sky)" stroke-width="4"/>
      <path d="M0 62 L540 62" stroke="var(--paper)" stroke-width="0" />
    </svg>
  </section>

</main>
</body>
</html>
```